BRIGHT COLORFUL + 55 FAMILY HISTORY BROCHURE 11 x 17 bifold

11 x 17 Bifold Flyer I have given you the Layout I just need you to make it Pretty

YOU DO NOT NEED TO FOLLOW MY LAYOUT, You can but dont have too

Target Market(s)

55 year old consumers, who could choose our service of Hereditary Cancer Screening

Industry/Entity Type

Health And Wellness

Requirements
Must have
• Must be appealing to Grand Parents, must make them want to test , show lots of pictures of grand children, YOU DO NOT NEED TO FOLLOW MY LAYOUT , You can but dont have too
Nice to have
• use our colors of our logo , YOU DO NOT NEED TO FOLLOW MY LAYOUT , You can but dont have too
Should not have
• YOU DO NOT NEED TO FOLLOW MY LAYOUT, You can but dont have too

```html
<!DOCTYPE html>
<html lang="en">
<head>
<meta charset="utf-8">
<title>Hereditary Cancer Screening Brochure</title>
<link href="https://fonts.googleapis.com/css2?family=Libre+Baskerville:wght@400;700&family=Arimo:wght@400;700&family=Didact+Gothic&display=swap" rel="stylesheet">
<style>
:root{
  --navy:#0f2a78;
  --blue:#1d55b0;
  --sky:#4aa3e0;
  --green:#7dc242;
  --ink:#3f3f3f;
  --bg:#d6d6d8;
  --paper:#ffffff;
}
*{box-sizing:border-box;margin:0;padding:0}
html,body{width:925px;height:1200px;overflow:hidden;background:var(--bg)}
body{position:relative;font-family:"Arimo",Arial,sans-serif;color:var(--ink)}
.spread{position:absolute;left:80px;width:776px;height:502px;background:var(--paper);box-shadow:0 10px 12px -6px rgba(0,0,0,.45);overflow:hidden}
.spread--outer{top:68px}
.spread--inner{top:630px}
.page{position:absolute;top:0;width:388px;height:502px;overflow:hidden}
.page--left{left:0;background:linear-gradient(90deg,#fff 85%,#e6e6e6)}
.page--right{left:388px;background:linear-gradient(90deg,#ececec,#fff 12%)}
.photo{position:absolute}
.photo--walk{background:
  radial-gradient(ellipse 40% 55% at 55% 60%,rgba(120,185,200,.75),transparent 70%),
  radial-gradient(ellipse 30% 40% at 30% 70%,rgba(236,214,205,.8),transparent 70%),
  radial-gradient(ellipse 25% 35% at 80% 75%,rgba(238,222,120,.75),transparent 70%),
  linear-gradient(180deg,#f4f6ee 0%,#b9d38c 35%,#7ea85a 70%,#c9c3a6 100%)}
.photo--family{background:
  radial-gradient(ellipse 30% 35% at 25% 35%,rgba(232,186,150,.85),transparent 70%),
  radial-gradient(ellipse 30% 35% at 70% 35%,rgba(230,185,152,.85),transparent 70%),
  radial-gradient(ellipse 35% 40% at 20% 80%,rgba(70,120,190,.8),transparent 70%),
  radial-gradient(ellipse 25% 35% at 75% 80%,rgba(205,50,110,.75),transparent 70%),
  radial-gradient(ellipse 25% 45% at 92% 55%,rgba(240,215,80,.8),transparent 70%),
  linear-gradient(180deg,#d8e6a6 0%,#b5cf6e 40%,#e6d9c2 100%)}
.photo--lawn{background:
  radial-gradient(ellipse 30% 40% at 20% 65%,rgba(170,195,230,.85),transparent 70%),
  radial-gradient(ellipse 30% 40% at 48% 50%,rgba(235,190,200,.85),transparent 70%),
  radial-gradient(ellipse 25% 35% at 70% 70%,rgba(240,228,220,.85),transparent 70%),
  radial-gradient(ellipse 20% 25% at 66% 90%,rgba(110,80,50,.6),transparent 70%),
  linear-gradient(180deg,#6c8a3e 0%,#a9c36a 35%,#d9c070 70%,#c9a550 100%)}
.photo--sofa{background:
  radial-gradient(ellipse 22% 40% at 15% 55%,rgba(232,196,170,.9),transparent 70%),
  radial-gradient(ellipse 22% 40% at 45% 60%,rgba(215,150,130,.85),transparent 70%),
  radial-gradient(ellipse 22% 40% at 72% 55%,rgba(230,190,175,.9),transparent 70%),
  radial-gradient(ellipse 18% 35% at 92% 60%,rgba(240,200,200,.85),transparent 70%),
  linear-gradient(180deg,#bcd17e 0%,#d9cfa6 45%,#d8b9a0 100%)}
.inset{position:absolute;border-radius:50%;border:4px solid var(--green)}
.inset--warm{background:radial-gradient(circle at 40% 45%,#f0d3bc,#dcb08e 55%,#b9c98a)}
.inset--hands{background:radial-gradient(circle at 50% 50%,#e8b895,#c5d8a0 65%,#8fb46a)}
.deco{position:absolute;inset:0;width:100%;height:100%}
.ribbon{position:absolute;border-radius:40% 40% 10% 10%;background:linear-gradient(135deg,#c98ad0,#6cc3ea)}
.serif{font-family:"Libre Baskerville",Georgia,serif}
.url{position:absolute;left:0;right:0;text-align:center;font-weight:700;font-size:11px;letter-spacing:.6px;color:var(--navy)}

/* outer left */
.risk-box{position:absolute;left:10px;top:236px;width:366px;height:134px;border-radius:6px;background:linear-gradient(100deg,var(--navy),var(--blue));color:#fff;padding:18px 12px;box-shadow:0 3px 6px rgba(0,0,0,.25)}
.risk-box h2{font-family:"Libre Baskerville",Georgia,serif;font-weight:400;font-size:13.5px;color:var(--green)}
.risk-box h2 b{font-weight:700}
.risk-box h3{font-family:"Libre Baskerville",Georgia,serif;font-weight:400;font-size:10.5px;margin-top:6px}
.risk-box hr{width:118px;border:0;border-top:1px solid #fff;margin:12px 0 8px}
.risk-box p{font-size:9.6px;line-height:15px;width:270px}
.intro{position:absolute;left:14px;top:392px;width:360px;font-size:7.6px;line-height:12px;text-align:justify}

/* outer right */
.brand{position:absolute;left:118px;top:22px;display:flex;align-items:center;gap:8px}
.brand__dot{width:48px;height:48px;border-radius:50%;background:var(--navy)}
.brand__name{font-family:"Libre Baskerville",Georgia,serif;font-size:15px;line-height:17px;color:var(--navy);letter-spacing:1px}
.cover-title{position:absolute;left:0;right:0;top:392px;text-align:center;font-size:22px;font-weight:400;color:var(--navy)}
.cover-tag{position:absolute;left:0;right:0;top:432px;text-align:center;font-family:"Didact Gothic",sans-serif;font-size:15px;color:var(--green);letter-spacing:.5px}

/* inner */
.inner-head{position:absolute;font-family:"Libre Baskerville",Georgia,serif;font-size:13px;font-weight:400;color:var(--navy)}
.knowledge{position:absolute;left:12px;top:214px;width:362px}
.knowledge .sub{font-size:10px;color:var(--green);margin-top:6px}
.knowledge p{font-size:7px;line-height:9px;margin-top:7px;text-align:justify}
.knowledge .lead{color:var(--navy)}
.blue{color:var(--navy)}
.callout{position:absolute;left:44px;top:436px;width:302px;height:39px;border:1px solid var(--green);border-radius:4px;text-align:center;font-weight:700;font-size:9.6px;line-height:14px;color:var(--green);padding-top:5px}
.stories{position:absolute;top:228px;font-size:7px;line-height:9.4px;text-align:justify}
.stories p{margin-bottom:8px}
.stories .g{color:var(--green)}
.stories .b{color:var(--navy)}
</style>
</head>
<body>

<section class="spread spread--outer">
  <article class="page page--left">
    <div class="photo photo--walk" style="left:0;top:0;width:388px;height:245px" role="img" aria-label="Photo of grandparents walking arm in arm with their grandchildren in a park"></div>
    <svg class="deco" viewBox="0 0 388 502" aria-hidden="true">
      <path d="M0 0H388V4C290 20 170 50 0 110Z" fill="#1d55b0"/>
      <path d="M0 110C170 50 290 20 388 4" fill="none" stroke="#7dc242" stroke-width="5"/>
      <path d="M0 0H330C250 10 150 35 0 80Z" fill="#0f2a78"/>
    </svg>
    <div class="risk-box">
      <h2><b>DOES CANCER</b> Run in Your Family?</h2>
      <h3><b>A Simple Swab</b> Could SAVE a Family Members LIFE</h3>
      <hr>
      <p>Your decision won't just affect you. It will also impact Your Family, since your test results may Forecast Their Cancer Risks, too.</p>
      <div class="ribbon" style="left:312px;top:8px;width:36px;height:72px" role="img" aria-label="Awareness ribbon"></div>
    </div>
    <p class="intro"><b>We believe it is important to understand what can and cannot be learned with genetic testing.</b> Genetic mutations can increase risks for certain cancers, but this does not mean cancer will definitely develop. You should be prepared to receive positive or negative results. <b>Most people receive Negative Results meaning no mutations associated with an increased risk for the Hereditary cancers.</b></p>
    <div class="url" style="top:468px">www.kinscreeninfo.com</div>
  </article>

  <article class="page page--right">
    <div class="photo photo--family" style="left:0;top:70px;width:388px;height:282px" role="img" aria-label="Photo of a smiling three-generation family with grandchildren sitting together outdoors"></div>
    <svg class="deco" viewBox="0 0 388 502" aria-hidden="true">
      <path d="M0 0H388V70C300 110 150 105 0 78Z" fill="#fff"/>
      <path d="M0 80C150 108 300 112 388 72" fill="none" stroke="#0f2a78" stroke-width="9"/>
      <path d="M0 92C150 118 300 120 388 84" fill="none" stroke="#7dc242" stroke-width="3"/>
      <path d="M0 330C120 350 260 350 388 300V502H0Z" fill="#fff"/>
      <path d="M0 330C120 350 260 350 388 300" fill="none" stroke="#7dc242" stroke-width="5"/>
    </svg>
    <div class="brand">
      <span class="brand__dot"></span>
      <span class="brand__name">CLEARPATH<br>HEALTH<br>GROUP</span>
    </div>
    <div class="ribbon" style="left:318px;top:42px;width:46px;height:104px" role="img" aria-label="Awareness ribbon"></div>
    <h1 class="cover-title serif">Hereditary Cancer Screening</h1>
    <div class="cover-tag">"The Test You Take For Them"</div>
    <div class="url" style="top:468px">www.kinscreeninfo.com</div>
  </article>
</section>

<section class="spread spread--inner">
  <article class="page page--left">
    <div class="photo photo--lawn" style="left:0;top:0;width:388px;height:182px" role="img" aria-label="Photo of grandparents with grandchildren and their dog on a sunny lawn"></div>
    <svg class="deco" viewBox="0 0 388 502" aria-hidden="true">
      <path d="M0 180C140 168 260 178 388 160V502H0Z" fill="#fff"/>
      <path d="M0 180C140 168 260 178 388 160" fill="none" stroke="#7dc242" stroke-width="4"/>
      <path d="M0 468C140 490 280 488 388 476V502H0Z" fill="#0f2a78"/>
      <path d="M0 466C140 486 280 484 388 472" fill="none" stroke="#7dc242" stroke-width="2"/>
    </svg>
    <div class="inset inset--warm" style="left:284px;top:122px;width:86px;height:86px" role="img" aria-label="Close-up photo of a grandmother hugging her granddaughter"></div>
    <div class="ribbon" style="left:326px;top:170px;width:36px;height:82px" role="img" aria-label="Awareness ribbon"></div>
    <div class="knowledge">
      <h2 class="inner-head" style="position:static">Give Them the Gift of Knowledge</h2>
      <div class="sub">Knowing is better than not knowing. <strong>Knowledge is Power</strong></div>
      <p class="lead">A Positive result or finding a mutation is Not a Cancer Diagnosis and does not mean you will ever develop Cancer learning if you have an increased risk for cancer can make a difference</p>
      <p><span class="blue">Genetic Testing</span> is done to determine whether family members without obvious illness have inherited the same mutation as a family member who is known to carry a cancer associated mutation. Meaning <strong>Will You Help Your Kids &amp; Grand Children</strong></p>
      <p><span class="blue">What are the benefits of testing?</span> "The Power of Knowledge" <strong>Helping Younger Family Members Know if there is a Risk and Preparing for it.</strong> Knowing if you have a genetic mutation is that you can work with your doctor to monitor and address your cancer risks. <strong>According to the National Wellness Council eating 5 or more servings of vegetables &amp; fruit, and most importantly also lowering your intake of red meat, dairy and eggs will help prevent or delay cancer.</strong></p>
      <p><span class="blue">There are many benefits to getting tested,</span> regardless of the eventual result. If one of your family members, however distant, had cancer, there is a chance that you inherited a gene mutation that not only increases your personal risk of cancer, but also could be passed to the next generation. Those who are carriers of hereditary cancer gene mutations could be at risk of getting cancer earlier in life than the general population.</p>
      <p class="blue"><strong>The sooner genetic testing is done, the more likely it is that the risk can be managed appropriately.</strong></p>
    </div>
    <div class="callout">There are many Known risk factors for Cancer.<br>GENETICS and FAMILY HISTORY are Often Overlooked.</div>
  </article>

  <article class="page page--right">
    <div class="photo photo--sofa" style="left:0;top:0;width:388px;height:176px" role="img" aria-label="Photo of a laughing family of three generations with grandchildren on a sofa"></div>
    <svg class="deco" viewBox="0 0 388 502" aria-hidden="true">
      <path d="M0 170C130 160 260 160 388 148V502H0Z" fill="#fff"/>
      <path d="M0 170C130 160 260 160 388 148" fill="none" stroke="#7dc242" stroke-width="4"/>
      <path d="M0 472C140 468 280 450 388 430V502H0Z" fill="#0f2a78"/>
      <path d="M0 468C140 464 280 446 388 426" fill="none" stroke="#7dc242" stroke-width="2"/>
    </svg>
    <h2 class="inner-head" style="left:15px;top:200px">Genetic Testing Saved My Life</h2>
    <div class="stories" style="left:15px;width:172px">
      <p class="g">Genetic testing revealed Daniel Marsh carried a mutation that gave him a 55 to 70 percent chance of developing stomach cancer. Early screening revealed there were 14 sites of stage 1A cancer. Once the news sunk in, he realized <strong class="b">his Mother Genetic Testing Saved His Life.</strong></p>
      <p><span class="b">Genetic Testing Saved My Life,</span> Because of my age and family ancestry, my doctor recommended Genetic Testing and they were right. I had the BRCA Gene, because of this my other two sisters got tested, my younger sister was positive and my older sister was negative. <strong>Now we are in control,</strong> there are steps that can be taken to reduce the risks, including enhanced breast cancer screening, risk-reducing surgeries, and chemoprevention, in which drugs are used to try to reduce the risk or delay the development of cancer.</p>
      <p><span class="b">A breast cancer survivor before age 30:</span> 'Genetic testing saved my life' Carla Benson was diagnosed with breast cancer two weeks before her 29th birthday.</p>
    </div>
    <div class="stories" style="left:204px;top:222px;width:176px">
      <p>Benson, now 30, credits her recovery to <strong>awareness of a hereditary genetic mutation</strong> that predisposed her and her family to the disease. <strong>After my mom tested positive for the BRCA 1 gene mutation,</strong> I knew genetic testing was something that I would need. <strong>Once I tested positive,</strong> I was referred to a breast health clinic for increased surveillance. There, my medical care providers were very diligent in making sure I was watched closely. Knowledge is power and, in this case, <strong>Genetic testing saved my life!</strong></p>
      <p><span class="b">My father had genetic testing</span> and found he had hereditary nonpolyposis colorectal cancer (HNPCC) commonly known as Lynch syndrome. My name is Helen Porter and I am a 10-year survivor of colorectal cancer. From an early age I learned the importance of screenings and knew about signs and symptoms. <strong>Following screening guidelines for individuals at an increased risk &amp; Knowing my family history saved my life!</strong></p>
    </div>
    <div class="inset inset--hands" style="left:240px;top:420px;width:58px;height:58px" role="img" aria-label="Photo of a child's hand holding a grandparent's hand"></div>
    <div class="inset inset--warm" style="left:302px;top:410px;width:76px;height:76px" role="img" aria-label="Photo of a grandfather with his granddaughter"></div>
    <div class="url" style="top:484px;color:#fff;text-align:left;left:104px">www.kinscreeninfo.com</div>
  </article>
</section>

</body>
</html>
```